Creative Bright Solar, Geothermal and Wind Website! GO GREEN

We are looking to reface our website. Brightfield energy partners of NY, LLC does Solar, Geothermal and Wind systems. Both on grid and off grid.
Im looking for a fun simple and informative website for customers to sign up for free quotes and see all our systems on a pin point map.
Solar is our main focus and we provide zero down financing with low monthly payments.

Main page should have three buttons to choose solar geo or wind.
"Get a FREE quote" visible and a spot to fill in name, phone, address, email and check boxes for solar geo and wind.

A map of New York that will include all of our systems we have done with a box stating the system size and link to a page with pictures and details of the system.

A meet the team drop down with bios on company employees.

Our current website : bfepofny.com

WE DONT WANT ANYTHING like it. Please. We need simple, fun, up to date, creative an colorful.

Thank you

Target Market(s)

Residential home owners, Commercial and Agricultural

Industry/Entity Type

Solar

Number of Pages Required

2 page

Requirements
Must have
• Map to show all projects completed
• 3 buttons Solar, Geothermal and Wind
• zero down financing
• Low monthly payments
• *** The ability to run the platform Joomla template on the web design.
Nice to have
• I added some pics, please use if you feel fit. your choice.
Should not have
• White background

```html
<!DOCTYPE html>
<html lang="en">
<head>
<meta charset="utf-8">
<title>Brightfield Energy Partners of NY, LLC</title>
<link href="https://fonts.googleapis.com/css2?family=Oswald:wght@400;500&family=Open+Sans:wght@400;600;700&display=swap" rel="stylesheet">
<style>
:root{
  --orange:#f7941d;
  --orange-light:#fbb04f;
  --orange-dark:#e07f0c;
  --green:#3f9a2b;
  --ink:#333333;
  --muted:#666666;
  --band:#ececec;
  --dark:#262626;
  --white:#ffffff;
  --hero-top:#5b8fc9;
  --hero-bottom:#a9c3dd;
}
*{box-sizing:border-box;margin:0;padding:0}
html,body{width:1200px;height:2284px;overflow:hidden}
body{font-family:"Open Sans",Arial,sans-serif;color:var(--ink);background:var(--band)}
.heading{font-family:"Oswald","Arial Narrow",sans-serif;font-weight:400}

/* header */
.site-header{height:112px;background:var(--white);position:relative}
.brand{position:absolute;left:128px;top:20px;display:flex;align-items:center;gap:14px}
.brand-mark{width:64px;height:64px;border-radius:50%;background:var(--orange)}
.brand-name{color:var(--green);font-weight:700;font-size:17px;line-height:22px}
.contact-phone{position:absolute;right:120px;top:20px;display:flex;align-items:center;gap:8px;font-size:17px;font-weight:600;color:var(--ink)}
.main-nav{position:absolute;right:104px;top:62px;display:flex;gap:36px;font-size:13px;font-weight:600;text-transform:uppercase;color:var(--muted)}
.main-nav a{text-decoration:none;color:inherit;padding-bottom:6px}
.main-nav a.active{color:var(--green);border-bottom:2px solid var(--green)}

/* hero */
.hero{height:528px;position:relative;background:linear-gradient(180deg,var(--hero-top) 0%,var(--hero-bottom) 100%)}
.hero-caption{position:absolute;left:0;right:0;bottom:0;height:68px;background:rgba(0,0,0,.35);color:var(--white);font-size:30px;text-align:center;line-height:68px}
.slider-arrow{position:absolute;top:312px;width:48px;height:48px;border-radius:50%;background:rgba(255,255,255,.55);display:flex;align-items:center;justify-content:center}
.slider-arrow.prev{left:88px}
.slider-arrow.next{right:88px}

/* welcome */
.welcome{height:320px;background:var(--band);position:relative}
.section-title{text-align:center;font-size:32px;color:var(--ink)}
.section-title::after{content:"";display:block;width:340px;height:2px;background:#9a9a9a;margin:8px auto 0}
.welcome .section-title{padding-top:30px}
.welcome-text{position:absolute;left:128px;top:112px;width:600px;font-size:13px;line-height:21px;color:var(--muted)}
.welcome-visual{position:absolute;left:790px;top:92px;width:290px;height:200px;border-radius:24px;background:radial-gradient(ellipse at 50% 50%,#cfdceb 0%,#9dbbd9 55%,var(--band) 100%)}

/* services */
.services{height:312px;background:var(--orange);display:flex;justify-content:center;gap:28px;padding-top:32px}
.service-button{width:232px;height:248px;background:var(--orange-light);display:flex;flex-direction:column;align-items:center;justify-content:center;gap:30px;color:var(--white);text-decoration:none}
.service-button span{font-family:"Oswald","Arial Narrow",sans-serif;font-size:30px}

/* inquiry */
.inquiry{height:320px;background:linear-gradient(135deg,#3a3a3a 0%,#1f1f1f 50%,#4a3f36 100%);position:relative}
.inquiry .heading{color:var(--white);font-size:32px;text-align:center;padding-top:30px}
.inquiry .heading::after{content:"";display:block;width:260px;height:2px;background:rgba(255,255,255,.7);margin:6px auto 0}
.inquiry-form{position:absolute;left:200px;top:110px;width:800px;display:grid;grid-template-columns:248px 252px 260px;column-gap:20px;row-gap:10px}
.field{height:30px;background:var(--white);border:1px solid #cfcfcf;font-size:12px;color:#888;padding:0 10px;display:flex;align-items:center;justify-content:space-between}
.field.message{grid-column:2 / span 2;grid-row:2 / span 2;height:70px;align-items:flex-start;padding-top:6px}
.submit{position:absolute;left:540px;top:240px;width:160px;height:34px;border:1px solid var(--orange-dark);background:linear-gradient(180deg,#ffc15a,var(--orange));color:var(--ink);font-weight:700;font-size:14px;display:flex;align-items:center;justify-content:center}

/* finance */
.finance{height:180px;background:var(--orange);display:flex;justify-content:center;align-items:center}
.finance-item{display:flex;align-items:center;gap:18px;width:400px;color:var(--white);font-weight:700;font-size:20px}
.finance-item:first-child{border-right:2px solid rgba(255,255,255,.7);margin-right:20px}

/* projects */
.projects{height:460px;background:var(--band);position:relative}
.projects .section-title{padding-top:28px}
.project-map{position:absolute;left:80px;top:84px;width:520px;height:352px;background:radial-gradient(ellipse at 55% 50%,#ffffff 0%,#e4e4e4 70%,var(--band) 100%)}
.project-photo{position:absolute;left:672px;top:92px;width:456px;height:200px;background:linear-gradient(160deg,#9cc3e6 0%,#3b5c8c 40%,#1e3763 70%,#8a8f96 100%)}
.project-title{position:absolute;left:672px;top:306px;width:456px;font-weight:700;font-size:18px;color:var(--ink)}
.project-text{position:absolute;left:672px;top:340px;width:456px;font-size:13px;line-height:20px;color:var(--muted)}

/* footer */
.site-footer{height:52px;background:var(--dark);color:#bbbbbb;font-size:12px;display:flex;justify-content:space-between;align-items:center;padding:0 124px}
</style>
</head>
<body>

<header class="site-header">
  <div class="brand">
    <div class="brand-mark"></div>
    <div class="brand-name">Brightfield Energy Partners<br>of NY, LLC</div>
  </div>
  <div class="contact-phone">
    <svg width="18" height="18" viewBox="0 0 24 24" aria-hidden="true"><path d="M6.6 10.8a15.2 15.2 0 006.6 6.6l2.2-2.2c.3-.3.7-.4 1-.2 1.1.4 2.3.6 3.6.6.6 0 1 .4 1 1V20c0 .6-.4 1-1 1A17 17 0 013 4c0-.6.4-1 1-1h3.5c.6 0 1 .4 1 1 0 1.3.2 2.5.6 3.6.1.3 0 .7-.2 1z" fill="#3f9a2b"/></svg>
    315 555 0142
  </div>
  <nav class="main-nav">
    <a class="active" href="#">Home</a>
    <a href="#">Solar Power</a>
    <a href="#">Wind Power</a>
    <a href="#">Installations</a>
    <a href="#">Contact Us</a>
  </nav>
</header>

<section class="hero" role="img" aria-label="Slider photograph: offshore wind turbines">
  <div class="slider-arrow prev"><svg width="18" height="18" viewBox="0 0 18 18"><path d="M12 2L5 9l7 7" stroke="#555" stroke-width="2.5" fill="none"/></svg></div>
  <div class="slider-arrow next"><svg width="18" height="18" viewBox="0 0 18 18"><path d="M6 2l7 7-7 7" stroke="#555" stroke-width="2.5" fill="none"/></svg></div>
  <p class="hero-caption heading">Lorem ipsum dolor sit amet consectetuer adipiscing elit sed</p>
</section>

<section class="welcome">
  <h2 class="section-title heading">Welcome To Brightfield Energy Partners</h2>
  <p class="welcome-text">Brightfield Energy Partners designs and installs solar, geothermal and wind systems for homes, farms and businesses across New York. Whether you want to stay on the grid or go fully off grid, our team plans every system around your site, your roof and your energy use. Solar is our main focus, and with zero down financing and low monthly payments, switching to clean power has never been easier. Ask for a free quote today and see how much you could save.</p>
  <div class="welcome-visual" role="img" aria-label="Illustration: light bulb holding a solar panel field"></div>
</section>

<section class="services">
  <a class="service-button" href="#">
    <svg width="96" height="80" viewBox="0 0 96 80" aria-hidden="true">
      <path d="M14 8h68l10 48H4z" fill="none" stroke="#fff" stroke-width="4"/>
      <path d="M37 8l-4 48M59 8l4 48M9 32h78" stroke="#fff" stroke-width="3"/>
      <path d="M48 56v16M32 74h32" stroke="#fff" stroke-width="4"/>
    </svg>
    <span>Solar</span>
  </a>
  <a class="service-button" href="#">
    <svg width="96" height="80" viewBox="0 0 96 80" aria-hidden="true">
      <path d="M20 40L48 16l28 24v12H20z" fill="#fff"/>
      <rect x="14" y="56" width="68" height="20" fill="none" stroke="#fff" stroke-width="3"/>
      <path d="M24 66c6-6 10 6 16 0s10 6 16 0 10 6 16 0" stroke="#fff" stroke-width="3" fill="none"/>
    </svg>
    <span>Geothermal</span>
  </a>
  <a class="service-button" href="#">
    <svg width="96" height="80" viewBox="0 0 96 80" aria-hidden="true">
      <path d="M46 30l-4 48h12l-4-48z" fill="#fff"/>
      <path d="M48 28L44 2l6 2z M48 28L26 44l0-7z M48 28l24 12-5 4z" fill="#fff" stroke="#fff" stroke-width="2" stroke-linejoin="round"/>
      <circle cx="48" cy="28" r="4" fill="#fff"/>
    </svg>
    <span>Wind</span>
  </a>
</section>

<section class="inquiry" role="group" aria-label="Quick inquiry form over a dim photograph of a keyboard">
  <h2 class="heading">Quick Inquiry</h2>
  <form class="inquiry-form">
    <div class="field">Name</div>
    <div class="field">Email</div>
    <div class="field">Phone</div>
    <div class="field">Location</div>
    <div class="field message">Message</div>
    <div class="field">Type <svg width="10" height="6" viewBox="0 0 10 6"><path d="M0 0h10L5 6z" fill="#777"/></svg></div>
  </form>
  <div class="submit">SUBMIT</div>
</section>

<section class="finance">
  <div class="finance-item">
    <svg width="40" height="40" viewBox="0 0 40 40" aria-hidden="true"><rect x="3" y="7" width="28" height="28" fill="none" stroke="#fff" stroke-width="3"/><path d="M10 20l7 7L36 4" stroke="#fff" stroke-width="4" fill="none"/></svg>
    Zero Down Financing
  </div>
  <div class="finance-item">
    <svg width="40" height="40" viewBox="0 0 40 40" aria-hidden="true"><rect x="3" y="7" width="28" height="28" fill="none" stroke="#fff" stroke-width="3"/><path d="M10 20l7 7L36 4" stroke="#fff" stroke-width="4" fill="none"/></svg>
    Low Monthly Payments
  </div>
</section>

<section class="projects">
  <h2 class="section-title heading">Our Completed Projects</h2>
  <div class="project-map" role="img" aria-label="Map of New York State with pins marking completed installations"></div>
  <div class="project-photo" role="img" aria-label="Photograph: installers fitting solar panels on a roof"></div>
  <h3 class="project-title">Lorem ipsum dolor sit amet, consectetuer</h3>
  <p class="project-text">A 9.6 kW rooftop solar array installed for a family home in the Finger Lakes region. The system covers most of their yearly electric use and was financed with zero down.</p>
</section>

<footer class="site-footer">
  <span>Home &nbsp;|&nbsp; Solar Power &nbsp;|&nbsp; Wind Power &nbsp;|&nbsp; Installations &nbsp;|&nbsp; Contact Us</span>
  <span>© 2015 Brightfield Energy Partners &nbsp;|&nbsp; All Rights Reserved</span>
</footer>

</body>
</html>
```